Gombrevo business card

Based on company logo and website given , to design a business card temple. Slogan "Your furry friends deserves the best"
Color style please refer to our website

```html
<!DOCTYPE html>
<html lang="en">
<head>
<meta charset="utf-8">
<title>Gombrevo business card</title>
<link href="https://fonts.googleapis.com/css2?family=Arimo:wght@400;700&display=swap" rel="stylesheet">
<style>
  :root {
    --backdrop: #e6e6e4;
    --card-light: #f7f7f7;
    --card-dark: #2a2a2a;
    --brand-blue: #1f5fb0;
    --accent-blue: #2b76c6;
    --text-grey: #555555;
    --rule-grey: #9a9a9a;
    --silver: #e4e4e4;
  }
  * { margin: 0; padding: 0; box-sizing: border-box; }
  html, body {
    width: 1200px; height: 801px; overflow: hidden;
    background: var(--backdrop);
    font-family: "Arimo", Arial, sans-serif;
  }
  .stage {
    position: relative; width: 1200px; height: 801px;
    display: flex; align-items: center; justify-content: center; gap: 40px;
  }
  .card {
    position: relative; width: 540px; height: 310px;
    border-bottom: 4px solid var(--brand-blue);
    box-shadow: 0 6px 18px rgba(0,0,0,0.18);
    overflow: hidden;
  }
  /* Front */
  .card-front { background: var(--card-light); }
  .front-brand {
    position: absolute; left: 40px; top: 128px; width: 220px;
    display: flex; align-items: center; gap: 10px;
  }
  .brand-mark { width: 18px; height: 18px; border-radius: 50%; background: var(--brand-blue); flex: none; }
  .brand-name { font-weight: 700; font-size: 38px; color: var(--brand-blue); letter-spacing: -0.5px; }
  .divider {
    position: absolute; left: 285px; top: 70px; width: 1px; height: 170px; background: var(--rule-grey);
  }
  .contact { position: absolute; left: 310px; top: 58px; width: 215px; color: var(--text-grey); }
  .person-name { font-weight: 700; font-size: 21px; color: var(--brand-blue); }
  .person-role { font-size: 13px; margin-top: 3px; }
  .address { font-size: 13px; line-height: 1.35; margin-top: 18px; }
  .contact-list { list-style: none; margin-top: 16px; font-size: 13px; }
  .contact-list li { display: flex; align-items: center; gap: 8px; margin-bottom: 7px; }
  .contact-list svg { width: 13px; height: 13px; flex: none; fill: var(--brand-blue); }
  .web-highlight { color: var(--brand-blue); }
  /* Back */
  .card-back { background: linear-gradient(160deg, #333 0%, var(--card-dark) 55%, #1f1f1f 100%); }
  .back-brand {
    position: absolute; left: 38px; top: 118px; display: flex; align-items: center; gap: 12px;
  }
  .back-brand .brand-mark { background: var(--silver); width: 22px; height: 22px; }
  .back-brand .brand-name { color: var(--silver); font-size: 50px; }
  .slogan { position: absolute; left: 40px; top: 186px; font-size: 17px; color: var(--accent-blue); }
</style>
</head>
<body>
<main class="stage">
  <section class="card card-front" aria-label="Business card front">
    <div class="front-brand">
      <span class="brand-mark"></span>
      <span class="brand-name">Gombrevo</span>
    </div>
    <div class="divider"></div>
    <div class="contact">
      <p class="person-name">Jonathan Smith</p>
      <p class="person-role">Manager</p>
      <p class="address">Your address, city<br>state, ZIP 0000</p>
      <ul class="contact-list">
        <li><svg viewBox="0 0 16 16"><path d="M3.5 1l3 3-1.8 1.8c.9 2 2.5 3.6 4.5 4.5L11 8.5l3 3-2 2.5C6.5 14 2 9.5 1 4z"/></svg>123-456-2100</li>
        <li><svg viewBox="0 0 16 16"><path d="M1 3h14v10H1zm1.5 1.2L8 8.6l5.5-4.4z" fill-rule="evenodd"/></svg>youremail@mailbox.com</li>
        <li><svg viewBox="0 0 16 16"><path d="M8 1a7 7 0 1 0 0 14A7 7 0 0 0 8 1zm0 2a5 5 0 1 1 0 10A5 5 0 0 1 8 3z"/><path d="M3 8h10v1H3zM7.5 3h1v10h-1z"/></svg><span>www.<span class="web-highlight">yourwebsite</span>.com</span></li>
      </ul>
    </div>
  </section>

  <section class="card card-back" aria-label="Business card back">
    <div class="back-brand">
      <span class="brand-mark"></span>
      <span class="brand-name">Gombrevo</span>
    </div>
    <p class="slogan">Your furry friends deserves the best</p>
  </section>
</main>
</body>
</html>
```